Cedar Gate Labradoodle web design

We're a new labradoodle breeder in Charleston, SC in need of a web design.

Our name is Cedar Gate Labradoodles.

Site we like: http://www.pebblefernlabradoodles.example/
http://www.quintbrookdoodles.example/

Logo Font:
The ''Cedar Gate'' font is called TestarossaNF and is available freely at http://www.typevatsample.example/veltrano-kx.font.  The ''Labradoodles'' font is called Worstveld Sling Extra and is available freely at http://www.glyphcrateonline.example/BrimholtDashHeavy.php.

Requirements
Must have
• Our logo
1. Home page
2. Labradoodle F.A.Q.
3. Our doodles
4. Availability
5. Adoption Process
6. Contact us
Link/badge icon for Health Guarantee
Nice to have
• Color and font to match the logo.

An area to add pictures
Should not have
• Rainbows
Rainbow colors

```html
<!DOCTYPE html>
<html lang="en">
<head>
<meta charset="utf-8">
<title>Cedar Gate Labradoodles</title>
<link rel="stylesheet" href="https://fonts.googleapis.com/css2?family=Federo&family=Open+Sans:wght@400;600&display=swap">
<style>
  :root {
    --page-bg: #0f0c0a;
    --footer-bg: #1d1d1e;
    --footer-line: #262627;
    --bottom-bg: #120e0b;
    --pink: #e0708f;
    --pink-light: #f08fab;
    --pink-dark: #b94a6a;
    --cream: #f1ddc9;
    --text: #f2f2f2;
    --muted: #9a9a9a;
    --field: #d2d2d2;
    --field-border: #9c9c9c;
    --icon-bg: #e9e9e9;
  }
  * { box-sizing: border-box; margin: 0; padding: 0; }
  html, body { width: 1200px; height: 986px; overflow: hidden; }
  body {
    position: relative;
    background: var(--page-bg);
    font-family: "Open Sans", Arial, sans-serif;
    color: var(--text);
  }
  .display { font-family: "Federo", Georgia, serif; font-variant: small-caps; }
  a { color: inherit; text-decoration: none; }

  /* Hero */
  .hero { position: absolute; left: 198px; top: 0; width: 801px; height: 421px; overflow: hidden; }
  .hero-photo {
    position: absolute; inset: 0;
    background:
      radial-gradient(ellipse 230px 260px at 260px 250px, #d9c7a6 0%, #b49d78 45%, rgba(60,45,30,0.6) 75%, rgba(0,0,0,0) 100%),
      radial-gradient(circle 40px at 220px 30px, rgba(255,245,220,0.7), rgba(0,0,0,0)),
      radial-gradient(circle 40px at 430px 15px, rgba(255,245,220,0.7), rgba(0,0,0,0)),
      linear-gradient(90deg, #2a2520 0%, #1b1714 55%, #020202 75%, #000 100%);
  }
  .brand { position: absolute; left: 8px; top: 8px; width: 134px; display: flex; flex-direction: column; align-items: center; gap: 6px; }
  .brand-dot { width: 62px; height: 62px; border-radius: 50%; background: var(--pink); }
  .brand-name { font-family: "Federo", Georgia, serif; font-size: 15px; line-height: 17px; color: var(--cream); text-align: center; }

  .social { position: absolute; display: flex; gap: 4px; }
  .social span { display: block; width: 25px; height: 25px; border-radius: 3px; background: var(--icon-bg); border: 1px solid #bdbdbd; }
  .social-top { right: 0; top: 10px; }

  .main-nav {
    position: absolute; left: 382px; top: 64px; width: 419px; height: 36px;
    border-radius: 4px;
    background: linear-gradient(180deg, var(--pink-light) 0%, var(--pink) 50%, var(--pink-dark) 100%);
    display: flex; align-items: center; justify-content: center;
  }
  .main-nav a { font-size: 12px; color: #fff; padding: 0 5px; line-height: 12px; }
  .main-nav a + a { border-left: 1px dotted rgba(255,255,255,0.7); }

  .hero-title { position: absolute; left: 408px; top: 148px; width: 380px; font-size: 29px; line-height: 42px; color: var(--cream); letter-spacing: 0.3px; }
  .hero-more { position: absolute; left: 408px; top: 252px; font-size: 13px; color: var(--pink); }

  /* Feature columns */
  .feature { position: absolute; top: 444px; width: 170px; }
  .feature h2 { font-size: 13px; font-weight: 400; color: var(--cream); white-space: nowrap; }
  .feature-photo { margin-top: 19px; height: 96px; border: 2px solid var(--pink); }
  .feature p { margin-top: 28px; font-size: 11px; line-height: 18px; color: var(--text); }
  .feature .more { display: block; margin-top: 21px; text-align: right; font-size: 11px; color: var(--pink); padding-right: 3px; }

  /* Footer */
  .site-footer {
    position: absolute; left: 0; top: 721px; width: 1200px; height: 221px;
    background: repeating-linear-gradient(0deg, var(--footer-bg) 0 2px, var(--footer-line) 2px 3px);
  }
  .site-footer h3 { position: absolute; top: 24px; font-size: 14px; font-weight: 400; color: var(--pink); }
  .about-thumb { position: absolute; left: 198px; top: 52px; width: 64px; height: 64px; background: radial-gradient(circle at 50% 45%, #e8dccd, #a08a70 70%, #4a3c2e); }
  .about-text { position: absolute; left: 198px; top: 50px; width: 240px; font-size: 11.5px; line-height: 14px; color: var(--text); }
  .about-text .float { float: left; width: 68px; height: 66px; }
  .social-footer { left: 550px; top: 97px; }

  .contact-form { position: absolute; left: 793px; top: 51px; width: 171px; }
  .contact-form input, .contact-form textarea {
    display: block; width: 171px; background: var(--field); border: 1px solid var(--field-border);
    font-family: Arial, Helvetica, sans-serif; font-size: 10px; color: #333; padding: 0 9px; margin-bottom: 3px;
  }
  .contact-form input { height: 24px; }
  .contact-form textarea { height: 85px; padding-top: 10px; resize: none; }
  .contact-form button {
    margin-top: 2px; width: 69px; height: 25px; border: 1px solid #888; border-radius: 2px;
    background: linear-gradient(180deg, #8a8a8a, #555);
    font-family: "Federo", Georgia, serif; font-variant: small-caps; font-size: 13px; color: var(--pink);
  }

  .bottom-bar { position: absolute; left: 0; top: 942px; width: 1200px; height: 44px; background: var(--bottom-bg); }
  .copyright { position: absolute; left: 201px; top: 15px; font-family: Arial, Helvetica, sans-serif; font-size: 10px; color: var(--muted); }
</style>
</head>
<body>
  <header class="hero">
    <div class="hero-photo" role="img" aria-label="Photo of a cream labradoodle sitting under studio lights"></div>
    <div class="brand">
      <span class="brand-dot"></span>
      <span class="brand-name">Cedar Gate Labradoodles</span>
    </div>
    <div class="social social-top" aria-label="Social links">
      <span role="img" aria-label="Social link"></span>
      <span role="img" aria-label="Social link"></span>
      <span role="img" aria-label="Social link"></span>
      <span role="img" aria-label="Social link"></span>
    </div>
    <nav class="main-nav display">
      <a href="#">Home</a>
      <a href="#">Labradoodle</a>
      <a href="#">Availability</a>
      <a href="#">Contact Us</a>
      <a href="#">Adoption Process</a>
      <a href="#">F.A.Q.</a>
    </nav>
    <h1 class="hero-title display">Lorem ipsum dolor sit amet, consectetuer adipiscing elit.</h1>
    <a class="hero-more display" href="#">Read More...</a>
  </header>

  <section class="feature" style="left:198px">
    <h2 class="display">Lorem ipsum dolor sit amet</h2>
    <div class="feature-photo" role="img" aria-label="Photo of a labradoodle with plush toys and a DVD cover" style="width:160px;background:linear-gradient(135deg,#ffffff,#efe4d3 60%,#d9c4a2)"></div>
    <p>Lorem ipsum dolor sit amet, consectetuer adipiscing elit, sed diam nonummy nibh euismod..</p>
    <a class="more display" href="#">Read More.....</a>
  </section>
  <section class="feature" style="left:418px">
    <h2 class="display">Lorem ipsum dolor sit amet</h2>
    <div class="feature-photo" role="img" aria-label="Still from a television segment with a presenter and a labradoodle" style="width:160px;background:linear-gradient(180deg,#8ea7c8,#c9a37e 55%,#2d56b0 85%,#1f4aa8)"></div>
    <p>Lorem ipsum dolor sit amet, consectetuer adipiscing elit, sed diam nonummy nibh euismod..</p>
    <a class="more display" href="#">Read More.....</a>
  </section>
  <section class="feature" style="left:639px">
    <h2 class="display">Lorem ipsum dolor set</h2>
    <div class="feature-photo" role="img" aria-label="Partner artwork on a white background" style="width:138px;background:linear-gradient(135deg,#ffffff,#f4ecd8 60%,#e6d2a4)"></div>
    <p>Lorem ipsum dolor sit amet, consectetuer adipiscing, sed diam nonummy nibh eod..</p>
    <a class="more display" href="#">Read More.....</a>
  </section>
  <section class="feature" style="left:838px">
    <h2 class="display">Lorem ipsum dolor sit amet</h2>
    <div class="feature-photo" role="img" aria-label="Photo of an event welcome poster" style="width:160px;background:radial-gradient(ellipse at 55% 50%,#efe6cf,#8c6a2c 60%,#5a3f1c)"></div>
    <p>Lorem ipsum dolor sit amet, consectetuer adipiscing elit, sed diam nonummy nibh euismod..</p>
    <a class="more display" href="#">Read More.....</a>
  </section>

  <footer class="site-footer">
    <h3 class="display" style="left:199px">About Cedar Gate</h3>
    <div class="about-thumb" role="img" aria-label="Photo of a white labradoodle"></div>
    <p class="about-text"><span class="float"></span>Lorem ipsum dolor sit amet, consectetuer adipiscing elit, diam nonummy n deuismod tincidunt ut laoreet dolore magna aliquam erat volutpat. Lorem ipsum dolor sit amet, consectetuer adipiscing elit, sed diam nonummy nibh euismod..</p>

    <h3 class="display" style="left:551px">Social media</h3>
    <div class="social social-footer" aria-label="Social links">
      <span role="img" aria-label="Social link"></span>
      <span role="img" aria-label="Social link"></span>
      <span role="img" aria-label="Social link"></span>
      <span role="img" aria-label="Social link"></span>
    </div>

    <h3 class="display" style="left:793px">Contact Us</h3>
    <form class="contact-form">
      <input type="text" placeholder="Your Name...">
      <input type="email" placeholder="Email Address...">
      <textarea placeholder="Your Message Here"></textarea>
      <button type="button">Submit</button>
    </form>
  </footer>

  <div class="bottom-bar">
    <p class="copyright">Copyright © 2013 CedarGate.example</p>
  </div>
</body>
</html>
```